Management Company Needs Web Banners

We need a new set of pixtrel banners developed. Here is what we would like to have:

1. Connect the branding with tangram images from www.VelmarShifts.com
2. Have a "Call to Action" like a "LET'S TALK" Button

1. 728x90 Investments Need Expert Management.
2. 300x250 Senior Living Turnaround Experts
3. 728x90 KIRV Finds Lost Revenue in Senior Living Investments
4. 600x315 Senior Living Turnaround Experts

Target Market(s)

Private Equity, Health Care REITs, physicians, pharmacist, etc.

Industry/Entity Type

Management Consulting

Requirements
Must have
• A branding connection to https://www.VelmarShifts.com/

```html
<!DOCTYPE html>
<html lang="en">
<head>
<meta charset="utf-8">
<title>KIRV Management Banner</title>
<link href="https://fonts.googleapis.com/css2?family=Montserrat:wght@700&family=Open+Sans:wght@400;600&display=swap" rel="stylesheet">
<style>
  :root {
    --white: #ffffff;
    --ink-purple: #5a2d82;
    --photo-dark: #2a2624;
    --photo-mid: #4a3a30;
    --photo-warm: #7a4a2a;
    --stripe-grey: #cfcfcf;
    --stripe-orange: #f08a24;
    --stripe-teal: #1d8f9a;
    --text-light: #f4f1ec;
  }
  * { margin: 0; padding: 0; box-sizing: border-box; }
  html, body { width: 1200px; height: 148px; overflow: hidden; background: var(--white); }
  .banner { position: relative; width: 1200px; height: 148px; overflow: hidden; font-family: "Open Sans", Arial, sans-serif; }
  .banner-photo {
    position: absolute; inset: 0;
    background:
      radial-gradient(ellipse 260px 120px at 1080px 20px, rgba(200,120,60,0.45), transparent 70%),
      radial-gradient(ellipse 220px 100px at 560px 130px, rgba(150,110,80,0.35), transparent 70%),
      linear-gradient(90deg, var(--photo-mid) 0%, var(--photo-dark) 45%, var(--photo-dark) 70%, var(--photo-warm) 100%);
  }
  .banner-shapes { position: absolute; inset: 0; }
  .brand {
    position: absolute; left: 34px; top: 38px;
    display: flex; align-items: center; gap: 16px;
  }
  .brand-dot { width: 66px; height: 66px; border-radius: 50%; background: var(--ink-purple); }
  .brand-name {
    font-family: "Montserrat", Arial, sans-serif; font-weight: 700;
    font-size: 56px; letter-spacing: 2px; color: var(--ink-purple); line-height: 1;
  }
  .cta {
    position: absolute; left: 425px; top: 36px; width: 223px; height: 60px;
    border: 2px solid var(--white); color: var(--white);
    display: flex; align-items: center; justify-content: center;
    font-size: 26px; font-weight: 400; letter-spacing: 0.5px; text-decoration: none;
  }
  .message {
    position: absolute; left: 750px; width: 420px; top: 14px;
    text-align: center; color: var(--text-light);
  }
  .headline { font-size: 31px; font-weight: 400; line-height: 38px; }
  .site-url { margin-top: 8px; font-size: 20px; letter-spacing: 0.5px; }
</style>
</head>
<body>
<div class="banner">
  <div class="banner-photo" role="img" aria-label="Blurred photo of colourful tangram puzzle pieces on a dark table"></div>
  <svg class="banner-shapes" width="1200" height="148" viewBox="0 0 1200 148">
    <polygon points="0,0 362,0 285,148 0,148" fill="var(--white)"/>
    <polygon points="362,0 392,0 315,148 285,148" fill="var(--stripe-grey)" opacity="0.85"/>
    <polygon points="392,0 402,0 325,148 315,148" fill="var(--stripe-orange)"/>
    <polygon points="402,0 408,0 331,148 325,148" fill="var(--stripe-teal)"/>
  </svg>
  <div class="brand">
    <span class="brand-dot"></span>
    <span class="brand-name">KIRV</span>
  </div>
  <a class="cta" href="#">LET’S TALK</a>
  <div class="message">
    <p class="headline">Investments Need<br>Expert Management</p>
    <p class="site-url">www.velmarshifts.com</p>
  </div>
</div>
</body>
</html>
```